50% off blue price stickers - poster

I am looking for a poster to hang in our retail discount store that let's people know they take 50% off the marked price on anything with a blue price sticker. We try and tell them as they walk in but can't catch everyone. If they don't know, they don't see the value in the pricing. We mark the retail price with a blue price tag and they get 50% off that price. We sell items from wholesale clubs (Brindle, JETs Depot) and offer 50% off what they sell the items for. Clothes, Housewares, Kitchenware, Furniture, Bath and Body, Electronics, Jewelry - you name it.
Updates

Check out our Chirpbook page - Marla's Found Again, in Brentwood, California to learn more about us and our merchandise.

For poster size - we are looking at 20" wide by 30" long. Thank you.

Target Market(s)

Ages 35-50

Industry/Entity Type

Retail

Font styles to use
Serif

Requirements
Must have
• Store name - Marla's Found Again
Nice to have
• Not too cluttered - easy to read to get the point across quickly. Something that incorporates our logo - but doesn't have to stick with the red/black theme, especially if you are using blue themes in the poster. Maybe just use the theme of the logo so the fonts are similar....

```html
<!DOCTYPE html>
<html lang="en">
<head>
<meta charset="utf-8">
<title>Take 50% Off – Blue Price Tag Poster</title>
<link rel="stylesheet" href="https://fonts.googleapis.com/css2?family=Playfair+Display:wght@700;800;900&display=swap">
<style>
  :root {
    --page-bg: #ffffff;
    --poster-deep: #2f2a9e;
    --poster-mid: #2b55d6;
    --poster-glow: #5fc8ff;
    --headline: #ffffff;
    --band-bg: rgba(6, 10, 40, 0.9);
    --band-text: #ffffff;
    --accent-blue: #3d8cff;
    --store-name: #ffffff;
  }
  html, body {
    margin: 0;
    padding: 0;
    width: 1200px;
    height: 1000px;
    overflow: hidden;
    background: var(--page-bg);
  }
  .canvas {
    position: relative;
    width: 1200px;
    height: 1000px;
  }
  .poster {
    position: absolute;
    left: 488px;
    top: 331px;
    width: 225px;
    height: 338px;
    overflow: hidden;
    font-family: 'Playfair Display', serif;
    font-variant-numeric: lining-nums;
  }
  .poster-backdrop {
    position: absolute;
    inset: 0;
    background:
      radial-gradient(ellipse 55% 45% at 50% 42%, var(--poster-glow) 0%, rgba(60,140,240,0.6) 40%, rgba(43,85,214,0) 100%),
      linear-gradient(180deg, var(--poster-mid) 0%, #2a4fd0 55%, var(--poster-deep) 100%);
  }
  .headline {
    position: absolute;
    left: 0;
    width: 100%;
    margin: 0;
    text-align: center;
    color: var(--headline);
    font-weight: 900;
    line-height: 1;
    white-space: nowrap;
  }
  .headline-take { top: 47px; font-size: 59px; letter-spacing: 1px; }
  .headline-amount { top: 101px; font-size: 65px; }
  .headline-off { top: 155px; font-size: 83px; }
  .info-band {
    position: absolute;
    left: 0;
    top: 261px;
    width: 100%;
    height: 36px;
    background: var(--band-bg);
    display: flex;
    flex-direction: column;
    justify-content: center;
    align-items: center;
  }
  .info-band p {
    margin: 0;
    color: var(--band-text);
    font-weight: 800;
    font-size: 11px;
    line-height: 13px;
    letter-spacing: 0.6px;
    text-transform: uppercase;
    white-space: nowrap;
  }
  .accent-blue { color: var(--accent-blue); }
  .store-name {
    position: absolute;
    left: 0;
    top: 297px;
    width: 100%;
    height: 41px;
    margin: 0;
    display: flex;
    align-items: center;
    justify-content: center;
    color: var(--store-name);
    font-weight: 700;
    font-size: 15px;
    letter-spacing: 0.4px;
    white-space: nowrap;
  }
</style>
</head>
<body>
<div class="canvas">
  <div class="poster">
    <div class="poster-backdrop" role="img" aria-label="Abstract blue light background with soft glowing bokeh"></div>
    <p class="headline headline-take">TAKE</p>
    <p class="headline headline-amount">50%</p>
    <p class="headline headline-off">OFF</p>
    <div class="info-band">
      <p>The marked price</p>
      <p>of any <span class="accent-blue">blue</span> price tag</p>
    </div>
    <p class="store-name">Marla's Found Again</p>
  </div>
</div>
</body>
</html>
```